Orvella Aid Fund - New Website Design

I need a site that looks like this http://renwick-gives-now.org for boat donations. So please replace the cars with boats.

```html
<!DOCTYPE html>
<html lang="en">
<head>
<meta charset="utf-8">
<title>Orvella Aid Fund – Donate Boat to Charity</title>
<link href="https://fonts.googleapis.com/css2?family=Arimo:wght@400;700&family=Lato:wght@400;700&family=Bree+Serif&display=swap" rel="stylesheet">
<style>
:root{
  --coral:#f26a5f;
  --blue:#5a7bc0;
  --blue-dark:#4a68ab;
  --ink:#3a3a3a;
  --text:#4a4a4a;
  --muted:#777;
  --blush:#f2e6e0;
  --white:#fff;
  --line:#cfcfcf;
  --footer:#e6e6e6;
  --faq-dark:#3d423f;
}
*{box-sizing:border-box;margin:0;padding:0}
html,body{width:1200px;height:2534px;overflow:hidden}
body{position:relative;background:var(--white);font-family:"Lato",Arial,sans-serif;color:var(--text)}
.abs{position:absolute}

/* header */
.site-header{position:absolute;left:0;top:0;width:1200px;height:101px;background:var(--white)}
.brand{position:absolute;left:234px;top:30px;display:flex;align-items:center;gap:12px}
.brand-mark{width:36px;height:36px;background:var(--coral);border-radius:50%}
.brand-name{font:700 26px "Lato",sans-serif;color:var(--ink)}
.call{position:absolute;left:662px;top:30px;display:flex;align-items:center;gap:10px;font:400 20px "Arimo",sans-serif;color:var(--ink);white-space:nowrap}
.call-icon{width:32px;height:32px;border-radius:50%;background:var(--coral);display:flex;align-items:center;justify-content:center}
.btn-donate{position:absolute;left:917px;top:29px;width:138px;height:31px;background:var(--blue);color:var(--white);font:700 14px "Arimo",sans-serif;display:flex;align-items:center;justify-content:center;gap:8px;border-radius:2px}

/* nav */
.main-nav{position:absolute;left:0;top:101px;width:1200px;height:38px;background:var(--blue)}
.main-nav a{position:absolute;top:0;height:38px;color:var(--white);font:700 14px/38px "Arimo",sans-serif;text-decoration:none;text-align:center}
.main-nav .active{background:var(--coral)}

/* hero */
.hero-photo{position:absolute;left:0;top:139px;width:1200px;height:423px;background:linear-gradient(90deg,#c9d3da 0%,#e8e2d4 35%,#e9e0c6 70%,#d9cfb2 100%)}
.hero-title{position:absolute;right:467px;top:294px;text-align:right;font:700 35px/1.22 "Arimo",sans-serif;color:var(--coral)}
.hero-sub{position:absolute;right:467px;top:387px;font:400 17px "Arimo",sans-serif;color:#222}

/* form */
.pickup-form{position:absolute;left:757px;top:88px;width:298px;height:394px;background:var(--coral);border-radius:0 0 4px 4px;box-shadow:0 2px 6px rgba(0,0,0,.25)}
.pickup-form h2{height:60px;text-align:center;font:400 22px/60px "Bree Serif",serif;color:var(--white);border-bottom:1px solid rgba(255,255,255,.5)}
.form-label{position:absolute;left:14px;font:700 12px "Lato",sans-serif;color:var(--white)}
.field{position:absolute;height:28px;background:var(--white);border:1px solid #e0e0e0;font:400 10px/26px "Lato",sans-serif;color:#888;padding-left:8px}
.field.select::after{content:"▾";position:absolute;right:6px;color:#333}
.btn-submit{position:absolute;left:84px;top:329px;width:130px;height:32px;background:var(--blue);color:var(--white);font:700 12px/32px "Lato",sans-serif;text-align:center;border-radius:2px}

/* welcome */
.welcome{position:absolute;left:0;top:562px;width:1200px;height:347px;background:var(--blush);text-align:center}
.section-title{position:absolute;left:0;width:1200px;text-align:center;font:700 44px "Arimo",sans-serif;color:var(--ink)}
.section-title span{color:var(--coral)}
.divider{position:absolute;left:230px;width:768px;height:14px}
.divider::before,.divider::after{content:"";position:absolute;top:7px;width:340px;height:1px;background:var(--line)}
.divider::before{left:0}.divider::after{right:0}
.divider i{position:absolute;left:372px;top:0;width:24px;height:14px;background:var(--coral);border-radius:7px}
.welcome p{position:absolute;left:0;width:1200px;text-align:center;font:400 13px "Lato",sans-serif;color:var(--text)}
.btn-read{position:absolute;left:555px;top:261px;width:119px;height:35px;background:var(--blue);color:var(--white);font:400 15px/35px "Lato",sans-serif;border-radius:2px;text-align:center}

/* benefits */
.benefits{position:absolute;left:0;top:909px;width:1200px;height:738px;background:var(--white)}
.benefits .sub{position:absolute;left:0;width:1200px;text-align:center;font:700 22px "Arimo",sans-serif;color:#222}
.benefit-label{position:absolute;font:400 15px/1.5 "Arimo",sans-serif;color:#222}
.benefit-label.left{text-align:right}

/* faq */
.faq{position:absolute;left:0;top:1647px;width:1200px;height:665px;background:linear-gradient(90deg,#2e332f 0%,#4a5048 45%,#6b6a5e 80%,#8a8070 100%)}
.faq-photo{position:absolute;right:0;top:0;width:200px;height:665px;background:linear-gradient(90deg,rgba(120,110,95,0),rgba(170,150,130,.55))}
.faq-title{position:absolute;left:0;top:20px;width:1422px;text-align:center;font:400 40px "Bree Serif",serif;color:var(--white)}
.faq-title span{color:var(--coral)}
.faq-item{position:absolute;left:228px;width:720px;height:37px;background:#e8e8e8;border:2px solid #bdbdbd;border-radius:2px;font:400 13px/33px "Arimo",sans-serif;color:#333;padding-left:34px}
.faq-item::before{content:"+";position:absolute;left:12px;top:0;color:var(--blue);font:700 17px/33px "Arimo",sans-serif}
.faq-open{position:absolute;left:228px;top:1803px;width:720px;height:118px;border:2px solid #9a9a9a;border-radius:2px;background:rgba(60,64,60,.6)}
.faq-open .q{height:34px;background:var(--coral);font:700 14px/34px "Arimo",sans-serif;color:var(--white);padding-left:24px;position:relative}
.faq-open .q::before{content:"–";position:absolute;left:9px}
.faq-open .a{padding:12px;font:400 11px "Lato",sans-serif;color:var(--white)}

/* footer */
.site-footer{position:absolute;left:0;top:2312px;width:1200px;height:222px;background:var(--footer)}
.site-footer nav a{position:absolute;top:70px;font:400 21px "Arimo",sans-serif;color:#222;text-decoration:none}
.site-footer nav a.active{color:var(--coral)}
.copyright{position:absolute;left:0;top:130px;width:1200px;text-align:center;font:400 14px "Arimo",sans-serif;color:#555}
</style>
</head>
<body>

<header class="site-header">
  <div class="brand"><span class="brand-mark"></span><span class="brand-name">Orvella Aid Fund</span></div>
  <div class="call">
    <span class="call-icon"><svg width="16" height="16" viewBox="0 0 24 24"><path fill="#fff" d="M6.6 10.8a15 15 0 0 0 6.6 6.6l2.2-2.2c.3-.3.7-.4 1-.2 1.1.4 2.3.6 3.6.6.6 0 1 .4 1 1V20c0 .6-.4 1-1 1A17 17 0 0 1 3 4c0-.6.4-1 1-1h3.5c.6 0 1 .4 1 1 0 1.3.2 2.5.6 3.6.1.3 0 .7-.2 1z"/></svg></span>
    Call: 1-800-555-0142
  </div>
  <div class="btn-donate">Donate Now
    <svg width="16" height="16" viewBox="0 0 24 24"><path fill="#fff" d="M12 4a3 3 0 1 1 0 6 3 3 0 0 1 0-6zM3 16h4l4 2h5a1.5 1.5 0 0 1 0 3H9l-6-1z"/></svg>
  </div>
</header>

<nav class="main-nav">
  <a class="active" href="#" style="left:234px;width:100px">HOME</a>
  <a href="#" style="left:350px;width:96px">ABOUT US</a>
  <a href="#" style="left:480px;width:110px">GET STARTED</a>
  <a href="#" style="left:628px;width:106px">CONTACT US</a>
</nav>

<section class="hero">
  <div class="hero-photo" role="img" aria-label="Photo of a young child in a headscarf hugging a soft toy"></div>
  <h1 class="hero-title">Donate Boat to<br>Charity!</h1>
  <p class="hero-sub">Your boat can make a difference!</p>
</section>

<form class="pickup-form">
  <h2>Donation Pick Up Form</h2>
  <div class="form-label" style="top:67px">Contact Information</div>
  <div class="field" style="left:14px;top:92px;width:130px">First Name</div>
  <div class="field" style="left:154px;top:92px;width:130px">Last Name</div>
  <div class="field" style="left:14px;top:132px;width:130px">Zip Code</div>
  <div class="field" style="left:154px;top:132px;width:130px">Day Phone</div>
  <div class="field" style="left:14px;top:172px;width:270px">Email Address</div>
  <div class="form-label" style="top:212px">Auto Donation Information</div>
  <div class="field select" style="left:14px;top:240px;width:130px;color:#333">Choose Year</div>
  <div class="field select" style="left:154px;top:240px;width:130px;color:#333">Choose Make</div>
  <div class="field" style="left:14px;top:283px;width:270px">Model of Boat</div>
  <div class="btn-submit">Submit Application</div>
</form>

<section class="welcome">
  <h2 class="section-title" style="top:50px">WELCOME TO <span>OAF</span></h2>
  <div class="divider" style="top:132px"><i></i></div>
  <p style="top:176px">Orvella Aid Fund's mission is to improve, empower and to bring joy to the lives of children and their families affected by cancer.</p>
  <p style="top:219px">OAF adapts its support to fit each child's needs; from education to assistance with treatment, recovery and family support.</p>
  <div class="btn-read">Read More</div>
</section>

<section class="benefits">
  <h2 class="section-title" style="top:83px">DONATE BOAT TO <span>CHARITY</span></h2>
  <p class="sub" style="top:140px">Your boat can make a difference!</p>
  <div class="divider" style="top:196px"><i></i></div>

  <svg class="abs" style="left:0;top:0" width="1200" height="738" viewBox="0 0 1200 738">
    <g stroke="#9fb1d8" stroke-width="2" fill="none">
      <line x1="415" y1="276" x2="500" y2="334"/>
      <line x1="364" y1="431" x2="460" y2="431"/>
      <line x1="415" y1="580" x2="500" y2="532"/>
      <line x1="792" y1="276" x2="708" y2="334"/>
      <line x1="840" y1="431" x2="748" y2="431"/>
      <line x1="792" y1="580" x2="708" y2="532"/>
    </g>
    <circle cx="604" cy="431" r="146" fill="#fff" stroke="#888" stroke-width="2" stroke-dasharray="2 3"/>
    <circle cx="604" cy="431" r="140" fill="#fff" style="filter:drop-shadow(0 3px 8px rgba(0,0,0,.15))"/>
    <rect x="588" y="395" width="32" height="32" fill="#f26a5f"/>
    <text x="604" y="462" text-anchor="middle" font-family="Lato,sans-serif" font-weight="700" font-size="20" fill="#3a3a3a">Orvella Aid Fund</text>
    <g fill="#fff" stroke="#5a7bc0" stroke-width="2">
      <circle cx="500" cy="334" r="6"/><circle cx="460" cy="431" r="6"/><circle cx="500" cy="532" r="6"/>
      <circle cx="708" cy="334" r="6"/><circle cx="748" cy="431" r="6"/><circle cx="708" cy="532" r="6"/>
    </g>
    <g fill="#fff" stroke="#dcdcdc" stroke-width="2">
      <circle cx="415" cy="276" r="46"/><circle cx="364" cy="431" r="46"/><circle cx="415" cy="580" r="46"/>
      <circle cx="792" cy="276" r="46"/><circle cx="840" cy="431" r="46"/><circle cx="792" cy="580" r="46"/>
    </g>
    <g fill="#5a7bc0">
      <circle cx="415" cy="276" r="39"/><circle cx="364" cy="431" r="39"/><circle cx="415" cy="580" r="39"/>
      <circle cx="792" cy="276" r="39"/><circle cx="840" cy="431" r="39"/><circle cx="792" cy="580" r="39"/>
    </g>
    <g fill="#fff"><rect x="393" y="268" width="26" height="14"/><path d="M419 270h10l6 7v5h-16z"/><circle cx="400" cy="285" r="4"/><circle cx="427" cy="285" r="4"/><path d="M393 268l-6-12h3l6 12z"/></g>
    <g fill="#fff"><path d="M340 434h48l-7 9h-36z"/><path d="M350 433v-8h18l8 8z"/></g>
    <g fill="#fff"><rect x="400" y="572" width="22" height="8" transform="rotate(-40 411 576)"/><rect x="410" y="578" width="4" height="18" transform="rotate(-40 412 587)"/><rect x="396" y="595" width="22" height="4"/><circle cx="430" cy="592" r="6"/></g>
    <path fill="#fff" d="M792 295c-16-11-22-18-22-26a10 10 0 0 1 22-4 10 10 0 0 1 22 4c0 8-6 15-22 26z"/>
    <g fill="#fff"><rect x="832" y="414" width="16" height="14"/><path d="M818 438h12l10 4h12l6-4 4 3-10 7h-18l-16-3z"/></g>
    <g fill="none" stroke="#fff" stroke-width="4"><path d="M803 568c-4-4-18-4-18 3s18 4 18 12-14 7-19 3"/><line x1="793" y1="560" x2="793" y2="600"/><line x1="774" y1="598" x2="812" y2="562"/></g>
  </svg>

  <p class="benefit-label left" style="left:200px;top:258px;width:155px">Free Towing In<br>24-48 Hours</p>
  <p class="benefit-label left" style="left:150px;top:413px;width:155px">We Accept<br>All Boats</p>
  <p class="benefit-label left" style="left:100px;top:563px;width:256px">Boats Will Be Sold on the<br>Largest Auction Network</p>
  <p class="benefit-label" style="left:855px;top:258px;width:220px">Boat Donations Help Fund<br>Charitable Programs</p>
  <p class="benefit-label" style="left:906px;top:413px;width:200px">Hassle<br>Free Donation</p>
  <p class="benefit-label" style="left:855px;top:563px;width:200px">Income<br>Tax Deduction</p>
</section>

<section class="faq" role="img" aria-label="Soft-focus background photo with a smiling child on the right">
  <div class="faq-photo"></div>
  <h2 class="faq-title">Frequently Asked <span>Questions</span></h2>
  <div class="divider" style="top:97px;left:372px;width:680px"><i style="left:328px"></i></div>
</section>
<div class="faq-open">
  <div class="q">What types of boats can be donated?</div>
  <div class="a">We accept all vehicle donations, and in most cases, we also accept boats, motorcycles, RV's, and campers.</div>
</div>
<div class="faq-item" style="top:1940px">What paperwork do I need to donate my boat?</div>
<div class="faq-item" style="top:1997px">Is my donated boat tax-deductible?</div>
<div class="faq-item" style="top:2055px">What if the boat is not registered in my name?</div>
<div class="faq-item" style="top:2112px">How much will I receive as a tax deduction for my boat?</div>
<div class="faq-item" style="top:2170px">When will I receive my tax receipt?</div>
<div class="faq-item" style="top:2228px">How do I schedule a pick up?</div>

<footer class="site-footer">
  <nav>
  <a class="active" href="#" style="left:237px">HOME</a>
  <a href="#" style="left:399px">ABOUT US</a>
  <a href="#" style="left:601px">GET STARTED</a>
  <a href="#" style="left:833px">CONTACT US</a>
  </nav>
  <p class="copyright">Copyright 2017 Orvella Aid Fund. All Rights Reserved.</p>
</footer>

</body>
</html>
```